BARRIER BANNER OTP

I am looking for a visual for a banner
3 meters long by 1 high.
In the same theme as the visual identity of the company.
As simple as possible without overloading

There must be the LOGO, the title TECHNIQUE SERVICES ROUSSEL

_________________________

I am looking for a visual for a banner (barrier banner)
3 meters long by 1 high.

AIR CONDITIONING HEATING VENTILATION
04 52 31 64 19

Font styles to use
Sans Serif

Colors
33b8a4
00a990
33a6d7
0493ce
3176b5
0355a3
ffffff

Requirements
Should not have
• No photo
No photo

```html
<!DOCTYPE html>
<html lang="fr">
<head>
<meta charset="utf-8">
<title>OTP – Banderoles</title>
<link href="https://fonts.googleapis.com/css2?family=Arimo:wght@700&family=Roboto:wght@500;700&display=swap" rel="stylesheet">
<style>
  :root {
    --backdrop: #a9a9a9;
    --logo-ink: #2f3d47;
    --teal: #00a990;
    --white: #ffffff;
  }
  html, body {
    margin: 0;
    width: 1013px;
    height: 1200px;
    overflow: hidden;
    background: var(--backdrop);
  }
  .banner {
    position: absolute;
    left: 84.4px;
    width: 843.6px;
    height: 281.4px;
    display: block;
  }
  .banner--title { top: 70px; }
  .banner--services { top: 451.4px; }
  .banner--contact { top: 825.2px; }
  .headline { font-family: "Arimo", Arial, sans-serif; font-weight: 700; fill: var(--white); }
  .copy { font-family: "Roboto", Arial, sans-serif; font-weight: 500; fill: var(--white); }
  .phone { font-family: "Roboto", Arial, sans-serif; font-weight: 700; }
  .phone--white { fill: var(--white); }
  .phone--teal { fill: var(--teal); }
  .brand-mark { font-family: "Roboto", Arial, sans-serif; font-weight: 700; fill: var(--logo-ink); }
  .brand-line { font-family: "Roboto", Arial, sans-serif; font-weight: 700; fill: var(--logo-ink); }
  .bullet { fill: var(--teal); }
  .panel-white { fill: var(--white); }
  .stripe-sheen { fill: var(--white); opacity: 0.03; }
</style>
</head>
<body>

<svg class="banner banner--title" viewBox="0 0 1469 490" aria-label="Banderole titre">
  <defs>
    <linearGradient id="navyFill" x1="0" y1="0" x2="1" y2="0">
      <stop offset="0" stop-color="#0d1627"/>
      <stop offset="0.5" stop-color="#1d2335"/>
      <stop offset="1" stop-color="#2a2f3b"/>
    </linearGradient>
    <linearGradient id="accentFill" gradientUnits="userSpaceOnUse" x1="601" y1="490" x2="938" y2="110">
      <stop offset="0" stop-color="#4cc08a"/>
      <stop offset="0.55" stop-color="#2ea9a8"/>
      <stop offset="1" stop-color="#2a93c8"/>
    </linearGradient>
  </defs>
  <rect class="panel-white" width="1469" height="490"/>
  <polygon fill="url(#navyFill)" points="0,0 1011,0 686,490 0,490"/>
  <polygon class="stripe-sheen" points="260,0 405,0 80,490 0,490 0,390"/>
  <polygon class="stripe-sheen" points="405,0 625,0 400,490 230,490"/>
  <polygon fill="url(#accentFill)" points="856,110 938,110 686,490 601,490"/>
  <text class="headline" x="90" y="193" font-size="84">TECHNIQUE</text>
  <text class="headline" x="90" y="283" font-size="84">SERVICES</text>
  <text class="headline" x="90" y="373" font-size="84">ROUSSEL</text>
  <text class="brand-mark" x="1204" y="406" font-size="220" text-anchor="middle">OTP</text>
</svg>

<svg class="banner banner--services" viewBox="0 0 1469 490" aria-label="Banderole prestations">
  <rect class="panel-white" width="1469" height="490"/>
  <polygon fill="url(#navyFill)" points="0,0 1011,0 686,490 0,490"/>
  <polygon class="stripe-sheen" points="260,0 405,0 80,490 0,490 0,390"/>
  <polygon class="stripe-sheen" points="405,0 625,0 400,490 230,490"/>
  <polygon fill="url(#accentFill)" points="856,110 938,110 686,490 601,490"/>
  <text class="copy" x="63" y="89" font-size="37">CLIMATISATION</text>
  <text class="copy" x="102" y="136" font-size="37">POMPE A CHALEUR</text>
  <text class="copy" x="63" y="183" font-size="37">CHAUFFAGE</text>
  <text class="copy" x="102" y="230" font-size="37">VENTILATION</text>
  <text class="copy" x="63" y="367" font-size="26">INSTALLATION / MAINTENANCE / DEPANNAGE</text>
  <text class="phone phone--white" x="331" y="436" font-size="46" text-anchor="middle">04 52 31 64 19</text>
  <text class="brand-mark" x="1219" y="308" font-size="215" text-anchor="middle">OTP</text>
  <text class="brand-line" x="1409" y="432" font-size="40" text-anchor="end">TECHNIQUE SERVICES ROUSSEL</text>
</svg>

<svg class="banner banner--contact" viewBox="0 0 1469 490" aria-label="Banderole contact">
  <rect class="panel-white" width="1469" height="490"/>
  <polygon fill="url(#navyFill)" points="0,0 1011,0 686,490 0,490"/>
  <polygon class="stripe-sheen" points="260,0 405,0 80,490 0,490 0,390"/>
  <polygon class="stripe-sheen" points="405,0 625,0 400,490 230,490"/>
  <polygon fill="url(#accentFill)" points="856,110 938,110 686,490 601,490"/>
  <text class="copy" x="41" y="81" font-size="41">INSTALLATION / MAINTENANCE / DEPANNAGE</text>
  <text class="phone phone--teal" x="407" y="153" font-size="59" text-anchor="middle">04 52 31 64 19</text>
  <polygon class="bullet" points="56,266 67,277 56,288"/>
  <text class="copy" x="84" y="290" font-size="37">CLIMATISATION</text>
  <polygon class="bullet" points="56,313 67,324 56,335"/>
  <text class="copy" x="84" y="337" font-size="37">POMPE A CHALEUR</text>
  <polygon class="bullet" points="56,360 67,371 56,382"/>
  <text class="copy" x="84" y="384" font-size="37">CHAUFFAGE</text>
  <polygon class="bullet" points="56,407 67,418 56,429"/>
  <text class="copy" x="84" y="431" font-size="37">VENTILATION</text>
  <text class="brand-mark" x="1219" y="308" font-size="215" text-anchor="middle">OTP</text>
  <text class="brand-line" x="1409" y="432" font-size="40" text-anchor="end">TECHNIQUE SERVICES ROUSSEL</text>
</svg>

</body>
</html>
```